Nice, modern, and professional credit repair website

We're a new credit repair company and we need a website to inform our prospective clients about the service we provide. We wan't it to catch the attention of the people as well as it be informative of the different types of derogatory items that can be listed on a report. Please refer to ( www.pathtoprime.example ) for an idea of what I'm looking for.

Colors
0455a3
0293ce
33a6d7
ffffff

Requirements
Must have
• The website must include information regarding credit repair. We'd like the website to include modern colors similar to that of our logo.
A link to our Facebook page. Www.facebook.com/brevantaledgerpartners
A link to our Instagram page: @BrevantaLedgerPartners
A link to our Snapchat page: Brevanta-Ledger
Also, we'd like to have an area where clients would fill out basic information where we could reach out to them.
Nice to have
• Images of new homes, cars, credit cards (Should NOT endorse Quilo, TF, BRONT, or Palvenry.)

```html
<!DOCTYPE html>
<html lang="en">
<head>
<meta charset="utf-8">
<title>Brevanta Ledger Partners — Credit Repair</title>
<link rel="stylesheet" href="https://fonts.googleapis.com/css2?family=Montserrat:wght@500;600;700&family=Open+Sans:wght@400;600;700&display=swap">
<style>
:root{
  --navy:#0455a3;
  --sky:#0293ce;
  --light-blue:#33a6d7;
  --white:#ffffff;
  --ink:#1f1f24;
  --text:#555b66;
  --muted:#8a909a;
  --pale:#eef2f7;
  --hero-bg:#eef1f5;
  --footer:#2e2e31;
  --line:#d5d9df;
}
*{box-sizing:border-box;margin:0;padding:0}
html,body{width:1200px;height:4269px;overflow:hidden}
body{position:relative;background:var(--white);font-family:"Open Sans",sans-serif;color:var(--text)}
.abs{position:absolute}
.heading{font-family:"Montserrat",sans-serif;font-weight:700;color:var(--ink);text-align:center;font-size:39px;letter-spacing:.3px;position:absolute;left:0;width:1200px}
.heading span{color:var(--navy)}
.btn{position:absolute;display:flex;align-items:center;justify-content:center;background:var(--light-blue);color:var(--white);font-family:"Montserrat",sans-serif;font-weight:700;border-radius:40px;text-decoration:none;letter-spacing:.3px;white-space:nowrap}

/* top bar */
.topbar{top:0;left:0;width:1200px;height:37px;background:var(--navy)}
.topbar .social{left:110px;top:10px;display:flex;gap:14px}
.topbar .social i{display:block;width:16px;height:16px;border-radius:3px;background:var(--white)}
.topbar .contact{right:110px;top:8px;color:var(--white);font-size:16px;display:flex;gap:10px;align-items:center;white-space:nowrap}

/* header */
.header{top:37px;left:0;width:1200px;height:115px;background:var(--white)}
.brand{left:108px;top:30px;width:300px;display:flex;align-items:center;gap:10px;white-space:nowrap}
.brand i{flex:none;width:52px;height:52px;border-radius:50%;border:4px solid var(--navy);display:block}
.brand b{font-family:"Montserrat",sans-serif;font-weight:700;font-size:19px;color:var(--navy);letter-spacing:.5px}
.nav{left:447px;top:45px;display:flex;gap:24px;font-family:"Montserrat",sans-serif;font-weight:600;font-size:17px;color:var(--ink);white-space:nowrap}
.nav .active{color:var(--light-blue);position:relative}
.nav .active::after{content:"";position:absolute;left:4px;right:4px;top:27px;height:4px;border-bottom:3px solid var(--light-blue);border-radius:0 0 40px 40px}
.login{left:920px;top:68px;width:167px;height:50px;font-size:16px}

/* hero */
.hero{top:152px;left:0;width:1200px;height:750px;background:var(--hero-bg);overflow:hidden}
.hero-photo{position:absolute;left:600px;top:0;width:600px;height:750px;background:linear-gradient(135deg,#b9c3c9 0%,#8d969a 45%,#4a4f55 100%)}
.hero-shape{position:absolute;left:0;top:0}
.hero h1{position:absolute;left:111px;top:125px;font-family:"Montserrat",sans-serif;font-weight:700;font-size:56px;line-height:66px;color:var(--ink);white-space:nowrap}
.hero h1 span{display:block;color:var(--navy);font-size:45px;font-weight:600}
.hero p{position:absolute;left:111px;top:278px;font-size:23px;line-height:40px;color:#4b4f57}
.hero .cta{left:111px;top:401px;width:224px;height:65px;font-size:21px}
.arrow{position:absolute;top:282px;width:43px;height:60px;background:#9aa0a6;display:flex;align-items:center;justify-content:center}

/* steps */
.step{position:absolute;top:925px;width:330px}
.step .num{position:absolute;left:0;top:36px;font-family:"Montserrat",sans-serif;font-weight:500;font-size:96px;line-height:96px;color:var(--white);-webkit-text-stroke:3px var(--navy)}
.step svg{position:absolute;left:78px;top:0}
.step h3{position:absolute;left:97px;top:204px;font-family:"Montserrat",sans-serif;font-weight:700;font-size:22px;color:var(--navy)}
.step p{position:absolute;left:98px;top:243px;width:220px;font-size:14px;line-height:28px;color:var(--muted)}

/* help */
.help{top:1321px;left:0;width:1200px;height:729px;background:var(--pale)}
.card{position:absolute;width:302px;height:223px;background:var(--white);text-align:center;box-shadow:0 2px 6px rgba(0,0,0,.05)}
.card svg{position:absolute;left:129px;top:30px}
.card h3{position:absolute;top:97px;left:0;width:100%;font-family:"Montserrat",sans-serif;font-weight:600;font-size:22px;color:var(--ink)}
.card p{position:absolute;top:137px;left:26px;width:250px;font-size:14px;line-height:27px;color:var(--muted)}
.card.featured{background:var(--light-blue)}
.card.featured h3,.card.featured p{color:var(--white)}

/* pricing */
.plan{position:absolute;top:2186px;width:295px;height:415px;background:var(--white);box-shadow:0 0 12px rgba(0,0,0,.12)}
.plan h3{position:absolute;top:25px;left:0;width:100%;text-align:center;font-family:"Montserrat",sans-serif;font-weight:600;font-size:25px;color:#333}
.plan .price{position:absolute;top:76px;left:0;width:100%;height:63px;background:var(--navy);color:var(--white);display:flex;align-items:baseline;justify-content:center;gap:10px;padding-top:10px}
.plan .price b{font-family:"Montserrat",sans-serif;font-size:34px}
.plan .price small{font-family:"Montserrat",sans-serif;font-size:18px;font-weight:500}
.plan ul{position:absolute;top:166px;left:22px;list-style:none}
.plan li{font-size:14px;line-height:33.4px;color:#6a707a;display:flex;align-items:center;gap:12px;white-space:nowrap}
.plan .buy{left:63px;top:391px;width:171px;height:54px;font-size:19px}
.plan.mid .price{background:var(--light-blue)}

/* banner */
.banner{top:2706px;left:0;width:1200px;height:384px;background:var(--navy);overflow:hidden}
.banner h2{position:absolute;top:58px;left:0;width:100%;text-align:center;font-family:"Montserrat",sans-serif;font-weight:700;font-size:40px;color:var(--white)}
.banner p{position:absolute;top:127px;left:200px;width:800px;text-align:center;font-size:14.5px;line-height:30px;color:var(--white)}
.banner .cta{left:386px;top:260px;width:428px;height:65px;font-size:20px}

/* contact */
.form-card{top:3240px;left:111px;width:978px;height:469px;background:var(--white);box-shadow:0 0 14px rgba(0,0,0,.12)}
.form-card .lead{position:absolute;top:48px;left:0;width:100%;text-align:center;font-family:"Montserrat",sans-serif;font-weight:500;font-size:21px;line-height:35px;color:var(--navy)}
.field{position:absolute;width:411px;height:51px;border:1px solid var(--line);font-size:15px;color:#8a8f97;padding:14px 19px}
.submit{left:403px;top:422px;width:172px;height:55px;font-size:19px}

/* footer */
.footer{top:3700px;left:0;width:1200px;height:569px}
.footer-bg{position:absolute;left:0;top:0}
.f-brand{left:111px;top:302px;width:300px;display:flex;align-items:center;gap:10px;white-space:nowrap}
.f-brand i{flex:none;width:54px;height:54px;border-radius:50%;border:4px solid var(--white);display:block}
.f-brand b{font-family:"Montserrat",sans-serif;font-weight:700;font-size:19px;color:var(--white);letter-spacing:.5px}
.f-about{left:111px;top:368px;width:300px;font-size:14px;line-height:25px;color:var(--white)}
.f-col h4{font-family:"Montserrat",sans-serif;font-weight:600;font-size:17px;color:var(--white);margin-bottom:20px;white-space:nowrap}
.f-col a,.f-col p{display:block;font-size:13.5px;line-height:27px;color:var(--white);text-decoration:none;white-space:nowrap}
.f-input{width:248px;height:36px;background:#5b5c60;color:var(--white);font-size:14px;display:flex;align-items:center;gap:10px;padding-left:14px;margin-top:14px}
.f-signup{position:relative;display:flex;width:130px;height:38px;margin-top:11px;font-size:14px}
.f-contact{left:890px;top:275px}
.f-contact div{display:flex;gap:12px;font-size:13.5px;line-height:22px;color:var(--white);margin-bottom:22px;white-space:nowrap}
.copy{left:113px;top:510px;font-size:13.5px;color:var(--white)}
.f-social{left:946px;top:494px;display:flex;gap:7px}
.f-social i{width:44px;height:44px;border-radius:50%;border:2px solid var(--white);display:block}
</style>
</head>
<body>

<!-- Top bar -->
<div class="abs topbar">
  <div class="abs social" aria-label="Social links"><i></i><i></i><i></i></div>
  <div class="abs contact">
    <svg width="16" height="12" viewBox="0 0 16 12"><rect width="16" height="12" rx="1" fill="#fff"/><path d="M1 1l7 6 7-6" stroke="#0455a3" stroke-width="1.6" fill="none"/></svg>
    <span>info@brevantaledger.example</span><span>|</span>
    <svg width="13" height="13" viewBox="0 0 24 24"><path fill="#fff" d="M6.6 10.8a15 15 0 006.6 6.6l2.2-2.2c.3-.3.7-.4 1-.2 1.1.4 2.3.6 3.6.6.6 0 1 .4 1 1V20c0 .6-.4 1-1 1A17 17 0 013 4c0-.6.4-1 1-1h3.5c.6 0 1 .4 1 1 0 1.3.2 2.5.6 3.6.1.3 0 .7-.2 1z"/></svg>
    <span>1 800 555 0142</span>
  </div>
</div>

<!-- Header -->
<header class="abs header">
  <div class="abs brand"><i></i><b>BREVANTA LEDGER</b></div>
  <nav class="abs nav">
    <span class="active">HOME</span><span>ABOUT</span><span>PRICING</span><span>BLOG</span><span>CONTACT US</span>
  </nav>
</header>
<a class="btn login">
  <svg width="14" height="14" viewBox="0 0 14 14" style="margin-right:8px"><circle cx="7" cy="4" r="3.2" fill="#fff"/><path d="M1 14c0-4 2.7-6 6-6s6 2 6 6z" fill="#fff"/></svg>CLIENT LOGIN</a>

<!-- Hero -->
<section class="abs hero">
  <div class="hero-photo" role="img" aria-label="Photo of a smiling woman at a laptop holding a credit card"></div>
  <svg class="hero-shape" width="1200" height="750" viewBox="0 0 1200 750">
    <polygon points="0,710 626,486 878,663 1200,467 1200,750 0,750" fill="#fff"/>
    <polyline points="315,596 626,486 878,663 1200,462" fill="none" stroke="#0455a3" stroke-width="8"/>
  </svg>
  <h1>BREVANTA<span>LEDGER PARTNERS</span></h1>
  <p>We're a new credit repair company.<br>We help improve your credit</p>
  <a class="btn cta">GET STARTED</a>
  <div class="arrow" style="left:0"><svg width="14" height="24"><path d="M12 2L3 12l9 10" stroke="#fff" stroke-width="3" fill="none"/></svg></div>
  <div class="arrow" style="right:0"><svg width="14" height="24"><path d="M2 2l9 10-9 10" stroke="#fff" stroke-width="3" fill="none"/></svg></div>
</section>

<!-- How credit repair works -->
<h2 class="heading" style="top:840px">HOW CREDIT <span>REPAIR WORKS</span></h2>

<div class="step" style="left:111px">
  <div class="num">1</div>
  <svg width="170" height="175" viewBox="0 0 170 175">
    <path d="M150 60A76 76 0 1 0 140 140" fill="none" stroke="#222" stroke-width="7"/>
    <path d="M60 160A76 76 0 0 0 150 115" fill="none" stroke="#0455a3" stroke-width="7"/>
    <rect x="60" y="66" width="42" height="42" rx="5" fill="none" stroke="#33a6d7" stroke-width="5"/>
    <path d="M74 96l4-12 26-26 8 8-26 26z" fill="#33a6d7"/>
  </svg>
  <h3>ENROLL</h3>
  <p>Duis aute irure dolor in repree nderit in voluptate velit esse cillum dolore eu fu</p>
</div>
<div class="step" style="left:436px">
  <div class="num">2</div>
  <svg width="170" height="175" viewBox="0 0 170 175">
    <path d="M150 60A76 76 0 1 0 140 140" fill="none" stroke="#222" stroke-width="7"/>
    <path d="M60 160A76 76 0 0 0 150 115" fill="none" stroke="#0455a3" stroke-width="7"/>
    <ellipse cx="80" cy="78" rx="24" ry="17" fill="none" stroke="#33a6d7" stroke-width="5"/>
    <path d="M66 92l-6 10 14-6" fill="#33a6d7"/>
    <path d="M94 100c12 0 22-6 22-15 0-4-2-8-6-11" fill="none" stroke="#33a6d7" stroke-width="5"/>
  </svg>
  <h3>DISPUTE</h3>
  <p>Duis aute irure dolor in repree nderit in voluptate velit esse cillum dolore eu fu</p>
</div>
<div class="step" style="left:772px">
  <div class="num">3</div>
  <svg width="170" height="175" viewBox="0 0 170 175">
    <path d="M150 60A76 76 0 1 0 140 140" fill="none" stroke="#222" stroke-width="7"/>
    <path d="M60 160A76 76 0 0 0 150 115" fill="none" stroke="#0455a3" stroke-width="7"/>
    <rect x="54" y="58" width="64" height="44" rx="4" fill="#33a6d7"/>
    <rect x="80" y="102" width="12" height="10" fill="#33a6d7"/>
    <rect x="70" y="111" width="32" height="5" rx="2" fill="#33a6d7"/>
  </svg>
  <h3>MONITOR</h3>
  <p>Duis aute irure dolor in repree nderit in voluptate velit esse cillum dolore eu fu</p>
</div>

<!-- How we can help -->
<section class="abs help">
  <h2 class="heading" style="top:56px">HOW WE CAN <span>HELP YOU</span></h2>

  <div class="card" style="left:111px;top:164px">
    <svg width="44" height="44" viewBox="0 0 44 44"><circle cx="22" cy="22" r="17" fill="none" stroke="#33a6d7" stroke-width="4"/><path d="M22 12v11h-7" stroke="#33a6d7" stroke-width="4" fill="none"/></svg>
    <h3>Late Payments</h3><p>Nemo enim ipsam voluptatem quia voluptas sit aspernatur aut</p>
  </div>
  <div class="card featured" style="left:449px;top:164px">
    <svg width="50" height="44" viewBox="0 0 50 44"><path d="M4 4h18l20 20-16 16L4 18z" fill="#fff"/><circle cx="12" cy="12" r="3.5" fill="#33a6d7"/><path d="M26 4l20 20-16 16" fill="none" stroke="#fff" stroke-width="3"/></svg>
    <h3>Tax Liens</h3><p>Nemo enim ipsam voluptatem quia voluptas sit aspernatur aut</p>
  </div>
  <div class="card" style="left:787px;top:164px">
    <svg width="52" height="44" viewBox="0 0 52 44"><rect x="2" y="8" width="48" height="28" rx="2" fill="#33a6d7"/><rect x="8" y="13" width="36" height="18" fill="#fff"/><circle cx="26" cy="22" r="7" fill="#33a6d7"/></svg>
    <h3>Charge offs</h3><p>Nemo enim ipsam voluptatem quia voluptas sit aspernatur aut</p>
  </div>
  <div class="card" style="left:111px;top:429px">
    <svg width="48" height="48" viewBox="0 0 48 48"><path d="M6 8h14l6 6v20H6z" fill="none" stroke="#33a6d7" stroke-width="3"/><path d="M20 18h14l8 8v20H20z" fill="#fff" stroke="#33a6d7" stroke-width="3"/></svg>
    <h3>Collection Accounts</h3><p>Nemo enim ipsam voluptatem quia voluptas sit aspernatur aut</p>
  </div>
  <div class="card" style="left:449px;top:429px">
    <svg width="44" height="44" viewBox="0 0 44 44"><rect x="4" y="4" width="36" height="36" rx="6" fill="#33a6d7"/><path d="M13 31l2-7 12-12 5 5-12 12z" fill="#fff"/></svg>
    <h3>Hard Inquiries</h3><p>Nemo enim ipsam voluptatem quia voluptas sit aspernatur aut</p>
  </div>
  <div class="card" style="left:787px;top:429px">
    <svg width="48" height="44" viewBox="0 0 48 44"><path d="M24 3l22 38H2z" fill="#33a6d7"/><rect x="21.5" y="15" width="5" height="14" fill="#fff"/><rect x="21.5" y="32" width="5" height="5" fill="#fff"/></svg>
    <h3>Bankruptcies</h3><p>Nemo enim ipsam voluptatem quia voluptas sit aspernatur aut</p>
  </div>
</section>

<!-- Pricing -->
<h2 class="heading" style="top:2098px">HOW MUCH <span>DOES IT COST?</span></h2>

<div class="plan" style="left:111px">
  <h3>BASIC</h3>
  <div class="price"><b>$99/m</b><small>Per Month</small></div>
  <ul>
    <li><svg width="15" height="12"><path d="M1 6l4.5 4.5L14 2" stroke="#0293ce" stroke-width="3" fill="none"/></svg>Unlimited Disputes</li>
    <li><svg width="15" height="12"><path d="M1 6l4.5 4.5L14 2" stroke="#0293ce" stroke-width="3" fill="none"/></svg>Unlimited Deletions</li>
    <li><svg width="15" height="12"><path d="M1 6l4.5 4.5L14 2" stroke="#0293ce" stroke-width="3" fill="none"/></svg>Flat Monthly Rate *No Contract*</li>
    <li><svg width="15" height="12"><path d="M1 6l4.5 4.5L14 2" stroke="#0293ce" stroke-width="3" fill="none"/></svg>24/7 Client Portal Access</li>
    <li><svg width="15" height="12"><path d="M1 6l4.5 4.5L14 2" stroke="#0293ce" stroke-width="3" fill="none"/></svg>Monthly Credit Analysis</li>
    <li><svg width="15" height="12"><path d="M1 6l4.5 4.5L14 2" stroke="#0293ce" stroke-width="3" fill="none"/></svg>Industry Leading Service</li>
  </ul>
  <a class="btn buy">GET STARTED</a>
</div>
<div class="plan mid" style="left:452px">
  <h3>MODERATE</h3>
  <div class="price"><b>$159/m</b><small>Per Month</small></div>
  <ul>
    <li><svg width="15" height="12"><path d="M1 6l4.5 4.5L14 2" stroke="#0293ce" stroke-width="3" fill="none"/></svg>Unlimited Disputes</li>
    <li><svg width="15" height="12"><path d="M1 6l4.5 4.5L14 2" stroke="#0293ce" stroke-width="3" fill="none"/></svg>Unlimited Deletions</li>
    <li><svg width="15" height="12"><path d="M1 6l4.5 4.5L14 2" stroke="#0293ce" stroke-width="3" fill="none"/></svg>Flat Monthly Rate *No Contract*</li>
    <li><svg width="15" height="12"><path d="M1 6l4.5 4.5L14 2" stroke="#0293ce" stroke-width="3" fill="none"/></svg>24/7 Client Portal Access</li>
    <li><svg width="15" height="12"><path d="M1 6l4.5 4.5L14 2" stroke="#0293ce" stroke-width="3" fill="none"/></svg>Monthly Credit Analysis</li>
    <li><svg width="15" height="12"><path d="M1 6l4.5 4.5L14 2" stroke="#0293ce" stroke-width="3" fill="none"/></svg>Industry Leading Service</li>
  </ul>
  <a class="btn buy">GET STARTED</a>
</div>
<div class="plan" style="left:792px">
  <h3>AGGRESSIVE</h3>
  <div class="price"><b>$399/m</b><small>Per Month</small></div>
  <ul>
    <li><svg width="15" height="12"><path d="M1 6l4.5 4.5L14 2" stroke="#0293ce" stroke-width="3" fill="none"/></svg>Unlimited Disputes</li>
    <li><svg width="15" height="12"><path d="M1 6l4.5 4.5L14 2" stroke="#0293ce" stroke-width="3" fill="none"/></svg>Unlimited Deletions</li>
    <li><svg width="15" height="12"><path d="M1 6l4.5 4.5L14 2" stroke="#0293ce" stroke-width="3" fill="none"/></svg>Flat Monthly Rate *No Contract*</li>
    <li><svg width="15" height="12"><path d="M1 6l4.5 4.5L14 2" stroke="#0293ce" stroke-width="3" fill="none"/></svg>24/7 Client Portal Access</li>
    <li><svg width="15" height="12"><path d="M1 6l4.5 4.5L14 2" stroke="#0293ce" stroke-width="3" fill="none"/></svg>Monthly Credit Analysis</li>
    <li><svg width="15" height="12"><path d="M1 6l4.5 4.5L14 2" stroke="#0293ce" stroke-width="3" fill="none"/></svg>Industry Leading Service</li>
  </ul>
  <a class="btn buy">GET STARTED</a>
</div>

<!-- Improve banner -->
<section class="abs banner">
  <h2>IMPROVE YOUR CREDIT SCORE</h2>
  <p>Nam libero tempore, cum soluta nobis est eligendi optio cumque nihil impedit quo minus id quod maxime placeat facere possimus, omnis voluptas assumenda est, omnis dolor repellendus. Temporibus autem quibusdam et aut officiis debitis aut rerum necessitatibus saepe eveniet</p>
  <a class="btn cta">SCHEDULE YOUR CONSULTATION</a>
</section>

<!-- Contact form -->
<h2 class="heading" style="top:3152px">CONTACT <span>FORM</span></h2>
<div class="abs form-card">
  <div class="lead">Fill out the following information to find out how<br>much fixing your credit could save you.</div>
  <div class="field" style="left:70px;top:149px">First Name</div>
  <div class="field" style="left:497px;top:149px">Last Name</div>
  <div class="field" style="left:70px;top:221px">Email Address</div>
  <div class="field" style="left:497px;top:221px">Phone No</div>
  <div class="field" style="left:70px;top:293px">Address</div>
  <div class="field" style="left:497px;top:293px">Zip Code</div>
  <a class="btn submit">SUBMIT</a>
</div>

<!-- Footer -->
<footer class="abs footer">
  <svg class="footer-bg" width="1200" height="569" viewBox="0 0 1200 569">
    <polygon points="0,244 320,42 575,220 1200,0 1200,569 0,569" fill="#2e2e31"/>
    <polyline points="0,244 320,42 575,220" fill="none" stroke="#0455a3" stroke-width="7"/>
  </svg>
  <div class="abs f-brand"><i></i><b>BREVANTA LEDGER</b></div>
  <p class="abs f-about">Nam libero tempore, cum soluta nobis est eli gendi optio cumque nihil impedit quo minus id quod maxime placeat facere possimus, omnis voluptas.</p>
  <div class="abs f-col" style="left:449px;top:275px">
    <h4>Quick Links</h4>
    <a>Blog</a><a>Credit Info</a><a>Privacy Policy</a><a>Terms &amp; Conditions</a><a>References</a>
  </div>
  <div class="abs f-col" style="left:608px;top:275px">
    <h4>Email Sign up</h4>
    <p style="line-height:23px">Enter your email address to get<br>information about us</p>
    <div class="f-input"><svg width="14" height="10"><rect width="14" height="10" fill="#fff"/><path d="M0 0l7 6 7-6" stroke="#5b5c60" fill="none"/></svg>Email address</div>
    <a class="btn f-signup"><svg width="14" height="14" viewBox="0 0 14 14" style="margin-right:8px"><path d="M1 13l1-4 8-8 3 3-8 8z" fill="#fff"/></svg>SIGN UP</a>
  </div>
  <div class="abs f-col f-contact">
    <h4>Contact Us</h4>
    <div><svg width="12" height="16" viewBox="0 0 12 16"><path d="M6 0a6 6 0 016 6c0 4-6 10-6 10S0 10 0 6a6 6 0 016-6z" fill="#33a6d7"/><circle cx="6" cy="6" r="2.2" fill="#2e2e31"/></svg><span>418 Harlow Street,<br>Fenwick, ST 20590</span></div>
    <div><svg width="13" height="13" viewBox="0 0 24 24"><path fill="#33a6d7" d="M6.6 10.8a15 15 0 006.6 6.6l2.2-2.2c.3-.3.7-.4 1-.2 1.1.4 2.3.6 3.6.6.6 0 1 .4 1 1V20c0 .6-.4 1-1 1A17 17 0 013 4c0-.6.4-1 1-1h3.5c.6 0 1 .4 1 1 0 1.3.2 2.5.6 3.6.1.3 0 .7-.2 1z"/></svg><span>1-800-555-0142</span></div>
    <div><svg width="15" height="11"><rect width="15" height="11" rx="1" fill="#33a6d7"/><path d="M1 1l6.5 5.5L14 1" stroke="#2e2e31" fill="none"/></svg><span>info@brevantaledger.example</span></div>
  </div>
  <p class="abs copy">© Copyright 2020: Brevanta Ledger Partners. All rights reserved</p>
  <div class="abs f-social" aria-label="Social links"><i></i><i></i><i></i></div>
</footer>

</body>
</html>
```